依頼詳細
①高校受験専門、②ウィークリーテストを行っている理由、③授業を受けるだけではいけない、④テスト期間は何回でも通塾可能といった碧陽舎ならではの部分を強く打ち出していけたらと考えております。

学年末テストのタイミング(2月中旬から3月にかけて予定)で、新聞折込やポスティングを考えております。

小学生、中1、中2の塾生に男の子が多いこともあり、特に女子生徒を持つご家庭に響くようなチラシデザインだとありがたいです!

授業風景の写真も出来るだけ使ってください!
記載項目
学習塾碧陽舎/〒318-0627 栃木県下野市梅ノ木町41-7/電話0285-61-4893/ホームページhttps://www.hekiyousha-example.net/本気で成績を上げたい子のための学習塾/料金などは付属のファイルから

塾説明会日程
3月4日(日)15:00~  3月10日(土)15:00~  3月21日(水/祝)15:00~  3月24日(土)15:00~  3月31日(土)15:00~
時間は45分ほどを想定しています。事前にご予約のお電話をお願い申し上げます。
説明会にご参加頂いた方は、入塾金10,800円を無料とさせていただきます!
サイズ
B4
ページ数
両面
希望イメージ
シンプル 複雑
単色 カラフル
暗い 明るい
日常 高級
遊び心 厳粛
未来的 伝統的
女性的 男性的
希望する色
赤系
納品ファイル
• 高解像度JPG (.jpg)
補足説明
開校一周年の部分を強調頂けると嬉しいです!
■ 選んだ理由

見出しの打ち出し方と表面にシンプルでありつつも情報量の多いところが気に入りました!

■ 提案者全員のお礼・コメント

たくさんのご提案ありがとうございました。

たくさん悩んだ末の決断でした。また夏の募集の時期などにチラシの作成をお願いすることあるかと思うので、その際にはよろしくお願いいたします!

```html
<!DOCTYPE html>
<html lang="ja">
<head>
<meta charset="utf-8">
<title>学習塾碧陽舎 次年度生徒募集</title>
<link href="https://fonts.googleapis.com/css2?family=Noto+Sans+JP:wght@400;500;700;900&family=Noto+Serif+JP:wght@300;700&display=swap" rel="stylesheet">
<style>
  :root{
    --red:#d7121b;
    --ink:#1a1a1a;
    --grey:#9a9a9a;
    --text:#333;
    --paper:#ffffff;
    --photo-a:#c9c2bd;
    --photo-b:#2c2f45;
  }
  *{margin:0;padding:0;box-sizing:border-box}
  html,body{width:849px;height:1200px;overflow:hidden;background:var(--paper)}
  body{font-family:"Noto Sans JP",sans-serif;color:var(--ink)}
  .flyer{position:relative;width:849px;height:1200px;overflow:hidden;background:var(--paper)}

  .headline{position:absolute;left:0;top:14px;width:100%;text-align:center;font-weight:900;letter-spacing:1px;line-height:1.1}
  .headline .line1{font-size:64px}
  .headline .line2{font-size:58px;margin-top:4px}
  .headline em{font-style:normal;color:var(--red)}
  .mark-square{display:inline-block;width:44px;height:44px;background:var(--red);vertical-align:-4px;margin-left:12px}

  .student-photo{position:absolute;left:280px;top:160px;width:290px;height:815px;
    background:linear-gradient(180deg,var(--photo-a) 0%,#8b7f79 30%,var(--photo-b) 60%,#3b3b4d 100%);
    border-radius:140px 140px 0 0}

  .anniversary{position:absolute;left:367px;top:500px;width:118px;height:118px;border-radius:50%;
    background:var(--red);color:#fff;text-align:center;border:3px solid #fff;box-shadow:0 0 0 2px var(--red)}
  .anniversary .small{font-size:10px;margin-top:14px;display:block}
  .anniversary .big{font-family:"Noto Serif JP",serif;font-weight:700;font-size:26px;line-height:1.05;display:block}

  .feature{position:absolute;width:250px;text-align:center}
  .feature .num{font-family:"Noto Serif JP",serif;font-weight:300;font-size:64px;color:var(--grey);line-height:1}
  .feature .label{font-size:11px;color:var(--red);margin-top:2px}
  .feature .label::before,.feature .label::after{content:"";display:inline-block;width:18px;height:1px;background:var(--red);vertical-align:middle;margin:0 6px}
  .feature h2{font-size:25px;font-weight:900;line-height:1.3;margin:12px 0 14px;color:var(--ink)}
  .feature h2 .accent{color:var(--red)}
  .feature p{font-size:11.5px;line-height:1.75;color:var(--text);text-align:left}
  .f1{left:22px;top:140px}
  .f2{left:580px;top:140px}
  .f3{left:22px;top:690px}
  .f4{left:580px;top:690px}

  .target-line{position:absolute;left:0;top:983px;width:100%;text-align:center;font-size:23px;font-weight:900;letter-spacing:1px;line-height:1.3}

  .recruit{position:absolute;left:24px;top:1022px;width:420px}
  .recruit .title{font-size:40px;font-weight:900;line-height:1.02;letter-spacing:2px}
  .recruit .title em{font-style:normal;color:var(--red)}
  .recruit .who{display:flex;align-items:center;margin-top:6px;font-size:10.5px;line-height:1.35}
  .recruit .tag{background:var(--ink);color:#fff;font-weight:700;padding:2px 6px;margin-right:8px}

  .brand{position:absolute;left:470px;top:1028px;width:355px;display:flex;align-items:center}
  .brand .square{width:72px;height:72px;background:var(--red);flex:none;margin-right:16px}
  .brand .names{flex:1}
  .brand .kind{background:var(--red);color:#fff;font-weight:900;font-size:22px;letter-spacing:14px;text-align:center;padding:2px 0}
  .brand .name{font-size:58px;font-weight:900;letter-spacing:10px;line-height:1.15;text-align:center}

  .info-band{position:absolute;left:0;top:1143px;width:100%;height:57px;background:var(--red);display:flex;align-items:center;padding:0 18px}
  .info-band .session{color:#fff;font-size:30px;font-weight:900;letter-spacing:2px;flex:none}
  .info-band .offer{margin-left:auto;background:#fff;height:40px;display:flex;align-items:center;padding:0 10px;font-weight:700}
  .offer .note{font-size:10px;line-height:1.3;margin-right:6px}
  .offer .fee{font-size:17px}
  .offer .fee em{font-style:normal;color:var(--red)}
  .offer .free{font-size:26px;font-weight:900;color:var(--red);margin-left:2px}
  .offer .more{font-size:9px;border:1px solid var(--ink);padding:2px 4px;margin-left:8px;line-height:1.2;text-align:center}
</style>
</head>
<body>
<main class="flyer">
  <header class="headline">
    <div class="line1"><em>本気</em>で<em>成績</em>を<em>上げたい</em></div>
    <div class="line2">子のための学習塾<span class="mark-square"></span></div>
  </header>

  <div class="student-photo" role="img" aria-label="鉛筆を前に差し出す制服姿の女子生徒の写真"></div>

  <div class="anniversary">
    <span class="small">おかげさまで</span>
    <span class="big">開校<br>1周年</span>
  </div>

  <section class="feature f1">
    <div class="num">1</div>
    <div class="label">碧陽舎の特徴</div>
    <h2>2中限定/地域密着<br><span class="accent">高校受験専門の塾</span></h2>
    <p>対象を地域の2中学校に絞り、それぞれの定期テストの傾向や進度を細かく把握しています。学校ごとの出題に合わせた指導で、内申点アップから志望校合格まで一貫してサポート。高校受験を見据えた学習計画を一人ひとりに合わせて作成し、着実に力を伸ばしていきます。</p>
  </section>

  <section class="feature f2">
    <div class="num">2</div>
    <div class="label">碧陽舎の特徴</div>
    <h2>苦手を把握する<br><span class="accent">ウィークリーテスト</span></h2>
    <p>毎週の小テストで理解度を確認し、つまずきをその場で見つけます。間違えた問題は解き直しまで行い、苦手をそのままにしません。結果は記録して面談で共有し、次の学習につなげます。</p>
  </section>

  <section class="feature f3">
    <div class="num">3</div>
    <div class="label">碧陽舎の特徴</div>
    <h2>授業を受けるだけで<br><span class="accent">終わらせない</span></h2>
    <p>授業で「分かった」を「できる」に変えるため、演習と確認を重ねます。自分で解ける力が身につくまで講師が丁寧に見守ります。</p>
  </section>

  <section class="feature f4">
    <div class="num">4</div>
    <div class="label">碧陽舎の特徴</div>
    <h2>充実のテスト対策<br><span class="accent">テスト期間中は<br>何回でも通塾可能</span></h2>
    <p>テスト前は自習室を開放し、質問にもすぐ対応します。追加料金なしで何回でも通えるので、安心して対策に集中できます。</p>
  </section>

  <div class="target-line">梅ノ木中、東陽中、東陽2中限定　高校受験専門塾</div>

  <section class="recruit">
    <div class="title"><em>次年度</em><br>生徒募集</div>
    <div class="who"><span class="tag">対象</span><span>上記中学に在籍の中学生<br>上記中学に進学予定の小学生</span></div>
  </section>

  <div class="brand">
    <div class="square"></div>
    <div class="names">
      <div class="kind">学習塾</div>
      <div class="name">碧陽舎</div>
    </div>
  </div>

  <footer class="info-band">
    <div class="session">塾説明会開催!</div>
    <div class="offer">
      <span class="note">説明会にご参加<br>頂いた方は、</span>
      <span class="fee">入塾金<em>(10,800円)</em>が</span>
      <span class="free">無料!</span>
      <span class="more">詳しくは<br>裏面へ</span>
    </div>
  </footer>
</main>
</body>
</html>
```